RV7 - Rapid Venture Harbor and Lantern

I need an introductory website for RV7 which describes the features of the product and the ease of use of the product. The product is focused on Preparing for an incident using Volunteer and Resource management and then responding to an incident with Incident Management, Team Management, Task Management and Communication Management. Once a situation is handled, the application provides complete reporting on each of the above aspects

Target Market(s)

Local Government entities, specifically the emergency department directors or coordinators

Industry/Entity Type

Government Office

Coding

Coded - Design and coding required

Font styles to use
Sans Serif

Requirements
Must have
• Clear layout with modern images. I want to be able to get a clear understanding of the features of the product and the ease of use. I would like to high light how the application helps in Communication Management, Team Management, Task Management and Incident Managements. Also, how the use of application helps to get an immediate snap shot of how well an incident was handled. I want to highlight how the Dashboard provides a quick look at the Incident(s) being managed
Nice to have
• I would like to in the future add videos to the site. At this point don't have any ideas about nice to have features
Should not have
• traditional designs. I am looking for a slick, modern looking website. Clean design is the key.

```html
<!DOCTYPE html>
<html lang="en">
<head>
<meta charset="utf-8">
<title>RV7 - Rapid Venture Harbor and Lantern</title>
<link href="https://fonts.googleapis.com/css2?family=Open+Sans:wght@400;600;700&family=Raleway:wght@600;700;800&display=swap" rel="stylesheet">
<style>
:root{
  --green:#8cc63f;
  --green-dark:#6fa62a;
  --blue:#1f5fb0;
  --blue-deep:#1a3f7a;
  --navy:#13284d;
  --ink:#222831;
  --text:#5b6168;
  --muted:#8a9096;
  --light:#f3f5f7;
  --white:#ffffff;
  --dark:#3a3d42;
}
*{box-sizing:border-box;margin:0;padding:0}
html,body{width:1200px;height:3432px;overflow:hidden}
body{font-family:"Open Sans",Arial,sans-serif;color:var(--text);background:var(--white);font-size:13px;line-height:1.6}
h1,h2,h3,h4{font-family:"Raleway","Open Sans",sans-serif;color:var(--ink)}
.wrap{width:1040px;margin:0 auto;position:relative}

/* header */
.site-header{height:88px;background:var(--white);border-bottom:1px solid #e6e8eb}
.site-header .wrap{display:flex;align-items:center;justify-content:space-between;height:88px}
.brand{display:flex;align-items:center;gap:12px}
.brand-mark{width:36px;height:36px;background:var(--blue)}
.brand-name{font-family:"Open Sans",sans-serif;font-weight:700;font-size:28px;color:var(--blue)}
.brand-tag{font-size:10px;color:var(--muted);margin-left:6px;line-height:1.2;width:150px}
.main-nav{display:flex;gap:0}
.main-nav a{font-size:11px;font-weight:600;color:var(--ink);text-decoration:none;padding:8px 14px;text-transform:uppercase}
.main-nav a.active{background:var(--blue);color:var(--white)}

/* hero */
.hero{height:472px;position:relative;background:#0f1418;overflow:hidden}
.hero-visual{position:absolute;inset:0;background:radial-gradient(ellipse at 68% 42%,#6fa8d8 0%,#2a4c6e 22%,#14212d 50%,#0c1116 80%)}
.hero .wrap{padding-top:130px}
.hero h1{color:var(--white);font-size:40px;font-weight:700;line-height:1.1}
.hero h2{color:var(--green);font-size:22px;font-weight:700;margin-top:6px}
.hero p{color:#c8ccd0;width:360px;margin-top:14px;font-size:12px}
.btn{display:inline-block;background:var(--green);color:var(--white);font-weight:700;font-size:11px;text-transform:uppercase;padding:10px 24px;text-decoration:none;margin-top:22px}
.hero-arrow{position:absolute;top:216px;width:30px;height:30px;border-radius:50%;border:2px solid rgba(255,255,255,.6);display:flex;align-items:center;justify-content:center}
.hero-arrow.left{left:24px}.hero-arrow.right{right:24px}

/* features */
.features{height:280px;display:flex;justify-content:center}
.feature{width:260px;height:280px;color:var(--white);text-align:center;padding:40px 26px 0}
.feature.green{background:var(--green)}
.feature.blue{background:var(--blue)}
.feature h3{color:var(--white);font-family:"Open Sans",sans-serif;font-weight:400;font-size:16px;line-height:1.3;margin-top:18px}
.feature p{font-size:11px;margin-top:12px;opacity:.9}

/* welcome */
.welcome{height:200px;text-align:center;padding-top:46px}
.welcome h2{font-size:26px;font-weight:700}
.welcome h3{font-size:18px;font-weight:700;margin-top:2px}
.welcome p{font-size:11px;margin:14px auto 0;width:980px;color:var(--muted)}

/* why */
.why{height:370px;position:relative;overflow:hidden}
.why-bg{position:absolute;inset:0;background:linear-gradient(100deg,#6e9c2f 0%,#8cc63f 45%,#a6d465 70%,#d9e8c4 100%)}
.why-phone{position:absolute;right:170px;top:40px;width:250px;height:320px;background:linear-gradient(160deg,#f4f6f8,#c7d2dc);border-radius:22px}
.why .wrap{padding-top:34px;color:var(--white)}
.why h2{color:var(--white);font-size:24px;font-weight:700}
.why .intro{width:520px;font-size:11px;margin-top:8px}
.why ul{list-style:none;margin-top:12px}
.why li{display:flex;align-items:center;gap:10px;font-size:12px;line-height:24px}

/* screens */
.screens{height:520px;text-align:center;padding-top:40px;background:var(--white)}
.screens h2{font-size:26px;font-weight:700}
.screens p{font-size:11px;color:var(--muted);width:900px;margin:10px auto 0}
.screens-shot{width:1040px;height:330px;margin:26px auto 0;background:linear-gradient(90deg,#dfe6ee 0%,#1f5fb0 30%,#2b6fc4 50%,#1f5fb0 70%,#eef2f6 100%)}

/* testimonials */
.testimonials{height:400px;position:relative;background:linear-gradient(180deg,#2b2e33,#45484e);color:#d7dadd;text-align:center;padding-top:78px}
.notch{position:absolute;top:0;left:50%;transform:translateX(-50%)}
.testimonials h2{color:var(--white);font-size:26px;font-weight:700}
.testimonials .rule{width:60px;height:2px;background:var(--green);margin:10px auto 0}
.quote{display:flex;align-items:center;gap:28px;width:860px;margin:40px auto 0;text-align:left}
.avatar{width:120px;height:120px;flex:none;border-radius:50%;border:4px solid var(--white);background:linear-gradient(160deg,#d9b48f,#8a6a52)}
.quote p{font-size:13px;line-height:1.7}
.quote cite{display:block;font-style:normal;font-size:11px;color:var(--green);font-weight:700;margin-top:10px}

/* volunteer */
.volunteer{height:556px;padding-top:46px;background:var(--white)}
.volunteer h2{text-align:center;font-size:26px;font-weight:700}
.cards{display:flex;gap:40px;justify-content:center;margin-top:36px}
.card{width:320px}
.card-photo{height:210px;background:linear-gradient(150deg,#cfd9e3,#7e93a8)}
.card h3{font-size:18px;font-weight:700;margin-top:18px}
.card p{font-size:11px;color:var(--muted);margin-top:8px}
.read-more{display:inline-block;font-size:10px;font-weight:700;color:var(--green);margin-top:12px;text-decoration:none}

/* newsletter */
.newsletter{height:96px;background:var(--blue)}
.newsletter .wrap{display:flex;align-items:center;height:96px;gap:18px}
.newsletter h3{color:var(--white);font-family:"Open Sans",sans-serif;font-size:15px;font-weight:600;width:360px}
.field{width:250px;height:34px;background:var(--white);font-size:11px;color:var(--muted);padding:8px 12px}
.subscribe{background:var(--green);color:var(--white);font-size:11px;font-weight:700;padding:9px 22px;height:34px}

/* footer */
.site-footer{height:410px;background:var(--blue-deep);color:#aebdd6}
.site-footer .wrap{display:flex;padding-top:54px;gap:60px}
.foot-brand{width:220px;display:flex;flex-direction:column;align-items:flex-start;gap:14px}
.foot-brand .brand-name{color:var(--white);font-size:36px}
.foot-brand .brand-mark{width:56px;height:56px;background:var(--white);opacity:.85}
.foot-col h4{font-family:"Open Sans",sans-serif;color:var(--green);font-size:13px;font-weight:700;margin-bottom:10px}
.foot-col ul{list-style:none;font-size:11px;line-height:22px}
.foot-col{width:160px}
.bottom-bar{height:40px;background:var(--navy);color:#7f90ad;font-size:10px}
.bottom-bar .wrap{display:flex;justify-content:space-between;align-items:center;height:40px}
</style>
</head>
<body>

<header class="site-header">
  <div class="wrap">
    <div class="brand">
      <span class="brand-mark"></span>
      <span class="brand-name">RV7</span>
      <span class="brand-tag">Rapid Venture Harbor and Lantern</span>
    </div>
    <nav class="main-nav">
      <a class="active" href="#">Home</a><a href="#">About Us</a><a href="#">Services</a><a href="#">Apps</a><a href="#">Blog</a><a href="#">Contact Us</a>
    </nav>
  </div>
</header>

<section class="hero">
  <div class="hero-visual" role="img" aria-label="Hand touching a tablet with a glowing globe and network lines above it"></div>
  <div class="wrap">
    <h1>RV7 - Rapid Venture</h1>
    <h2>Harbor and Lantern</h2>
    <p>Coordinate every responder, task and message from one clear dashboard built for local emergency teams and their directors.</p>
    <a class="btn" href="#">Get Started Now</a>
  </div>
  <span class="hero-arrow left"><svg width="10" height="12" viewBox="0 0 10 12"><path d="M8 1L2 6l6 5" fill="none" stroke="#fff" stroke-width="2"/></svg></span>
  <span class="hero-arrow right"><svg width="10" height="12" viewBox="0 0 10 12"><path d="M2 1l6 5-6 5" fill="none" stroke="#fff" stroke-width="2"/></svg></span>
</section>

<section class="features">
  <div class="feature green">
    <svg width="64" height="64" viewBox="0 0 64 64" fill="none" stroke="#fff" stroke-width="2"><circle cx="32" cy="32" r="30"/><path d="M32 14l14 5v11c0 10-6 16-14 20-8-4-14-10-14-20V19z"/><path d="M26 36v-8h12v8M32 24v-3"/></svg>
    <h3>Incident<br>Management</h3>
    <p>Log, track and close incidents with live status and a full audit trail for later review.</p>
  </div>
  <div class="feature blue">
    <svg width="64" height="64" viewBox="0 0 64 64" fill="none" stroke="#fff" stroke-width="2"><circle cx="32" cy="32" r="30"/><path d="M32 14l14 5v11c0 10-6 16-14 20-8-4-14-10-14-20V19z"/><circle cx="32" cy="27" r="4"/><path d="M25 39c1-5 13-5 14 0"/></svg>
    <h3>Team<br>Management</h3>
    <p>Build teams in seconds, assign roles and see who is on site at any moment.</p>
  </div>
  <div class="feature green">
    <svg width="64" height="64" viewBox="0 0 64 64" fill="none" stroke="#fff" stroke-width="2"><circle cx="32" cy="32" r="30"/><path d="M32 14l14 5v11c0 10-6 16-14 20-8-4-14-10-14-20V19z"/><path d="M24 32l16-7-5 16-3-6z"/></svg>
    <h3>Task<br>Management</h3>
    <p>Create, dispatch and follow each task from request to completion with clear priority.</p>
  </div>
  <div class="feature blue">
    <svg width="64" height="64" viewBox="0 0 64 64" fill="none" stroke="#fff" stroke-width="2"><circle cx="32" cy="32" r="30"/><path d="M32 14l14 5v11c0 10-6 16-14 20-8-4-14-10-14-20V19z"/><circle cx="32" cy="31" r="8"/><path d="M24 31h16M32 23c-4 5-4 11 0 16M32 23c4 5 4 11 0 16"/></svg>
    <h3>Communication<br>Management</h3>
    <p>Send alerts and updates to every team through one channel, logged and time stamped.</p>
  </div>
</section>

<section class="welcome">
  <h2>WELCOME TO RV7</h2>
  <h3>RV7 - Rapid Venture Harbor and Lantern</h3>
  <p>RV7 helps local government emergency departments prepare before an incident, respond while it unfolds and learn once it is over. Register volunteers and resources ahead of time, then manage incidents, teams, tasks and communication from a single dashboard. When the situation is handled, full reports on every area give directors an instant snapshot of how well the response went and where to improve next time.</p>
</section>

<section class="why">
  <div class="why-bg" role="img" aria-label="Responder using a phone, washed in green"></div>
  <div class="why-phone" role="img" aria-label="Smartphones showing the RV7 incident dashboard"></div>
  <div class="wrap">
    <h2>WHY ADOPT RV7</h2>
    <p class="intro">Built with coordinators, RV7 removes paperwork and guesswork so your people can focus on the response itself.</p>
    <ul>
      <li><svg width="14" height="14" viewBox="0 0 14 14"><path d="M2 7l3 3 7-7" fill="none" stroke="#fff" stroke-width="2"/></svg>Simple registration for volunteers and resources</li>
      <li><svg width="14" height="14" viewBox="0 0 14 14"><path d="M2 7l3 3 7-7" fill="none" stroke="#fff" stroke-width="2"/></svg>Live dashboard view of every active incident</li>
      <li><svg width="14" height="14" viewBox="0 0 14 14"><path d="M2 7l3 3 7-7" fill="none" stroke="#fff" stroke-width="2"/></svg>Instant alerts to teams on phone, tablet or desktop</li>
      <li><svg width="14" height="14" viewBox="0 0 14 14"><path d="M2 7l3 3 7-7" fill="none" stroke="#fff" stroke-width="2"/></svg>Clear task tracking from request to completion</li>
      <li><svg width="14" height="14" viewBox="0 0 14 14"><path d="M2 7l3 3 7-7" fill="none" stroke="#fff" stroke-width="2"/></svg>Team rosters with roles, skills and availability</li>
      <li><svg width="14" height="14" viewBox="0 0 14 14"><path d="M2 7l3 3 7-7" fill="none" stroke="#fff" stroke-width="2"/></svg>Complete reports once the situation is handled</li>
      <li><svg width="14" height="14" viewBox="0 0 14 14"><path d="M2 7l3 3 7-7" fill="none" stroke="#fff" stroke-width="2"/></svg>Secure access for every level of your department</li>
      <li><svg width="14" height="14" viewBox="0 0 14 14"><path d="M2 7l3 3 7-7" fill="none" stroke="#fff" stroke-width="2"/></svg>Easy to learn, with no lengthy training required</li>
    </ul>
  </div>
</section>

<section class="screens">
  <h2>APPLICATION SCREENS</h2>
  <p>A quick look at the screens your coordinators will use every day: incident map, navigation menu, notifications and the live feed of tasks and teams.</p>
  <div class="screens-shot" role="img" aria-label="Application screens: incident map, side menu, notifications list and task feed"></div>
</section>

<section class="testimonials">
  <svg class="notch" width="60" height="24" viewBox="0 0 60 24"><path d="M0 0h60L30 24z" fill="#ffffff"/></svg>
  <h2>TESTIMONIALS</h2>
  <div class="rule"></div>
  <div class="quote">
    <div class="avatar" role="img" aria-label="Portrait of the quoted coordinator"></div>
    <div>
      <p>&ldquo;RV7 gave our department one shared picture of every incident. Teams get their tasks instantly, messages never go missing, and the reports afterwards show exactly how well we responded and what to train for next.&rdquo;</p>
      <cite>DANA WHITFIELD, EMERGENCY COORDINATOR</cite>
    </div>
  </div>
</section>

<section class="volunteer">
  <h2>VOLUNTEER AND RESOURCE MANAGEMENT</h2>
  <div class="cards">
    <article class="card">
      <div class="card-photo" role="img" aria-label="Volunteers gathered around a table planning"></div>
      <h3>Sed ut perspiciatis unde</h3>
      <p>Register volunteers with skills and availability so the right people are ready before any incident begins.</p>
      <a class="read-more" href="#">READ MORE</a>
    </article>
    <article class="card">
      <div class="card-photo" role="img" aria-label="Coordinators reviewing resources on a laptop"></div>
      <h3>Sed ut perspiciatis unde</h3>
      <p>Keep an up to date list of vehicles, equipment and supplies, and see at a glance what is free to deploy.</p>
      <a class="read-more" href="#">READ MORE</a>
    </article>
    <article class="card">
      <div class="card-photo" role="img" aria-label="Team meeting in an office briefing room"></div>
      <h3>Sed ut perspiciatis unde</h3>
      <p>Match people and resources to incidents in a few taps, then review usage in the final reports.</p>
      <a class="read-more" href="#">READ MORE</a>
    </article>
  </div>
</section>

<section class="newsletter">
  <div class="wrap">
    <h3>SUBSCRIBE RV7 NEWSLETTER</h3>
    <div class="field">Name</div>
    <div class="field">Email Address</div>
    <div class="subscribe">SUBSCRIBE</div>
  </div>
</section>

<footer class="site-footer">
  <div class="wrap">
    <div class="foot-brand">
      <span class="brand-mark"></span>
      <span class="brand-name">RV7</span>
    </div>
    <div class="foot-col"><h4>Links</h4><ul><li>Home</li><li>About Us</li><li>Services</li><li>Apps</li><li>Blog</li><li>Contact Us</li></ul></div>
    <div class="foot-col"><h4>Incident</h4><ul><li>Raise new incident</li><li>Incident dashboard</li><li>Team updates</li><li>Task feed</li><li>Reports</li></ul></div>
    <div class="foot-col"><h4>Volunteer</h4><ul><li>Register volunteer</li><li>Skills directory</li><li>Resource list</li><li>Availability</li></ul></div>
    <div class="foot-col"><h4>Contact</h4><ul><li>12 Lantern Quay</li><li>Harbor District</li><li>+00 555 0147 220</li><li>hello@rv7-harbor.test</li></ul></div>
  </div>
</footer>

<div class="bottom-bar">
  <div class="wrap">
    <span>&copy; RV7 - Rapid Venture Harbor and Lantern. All rights reserved.</span>
    <span>Privacy &middot; Terms</span>
  </div>
</div>

</body>
</html>
```